Velmora Care! Create an exciting flyer for our hemodialysis clinic

Create an engaging Flyer that shows our offering and that will drive patients to our hemodialysis clinic. www.velmoracare.example

Target Market(s)

Mass public

Industry/Entity Type

Healthcare

Requirements
Must have
• 1 Our logo. 2. Should include that we accept all insurances 3. Our tag line “Transforming Lives, One Dialysis Session at a Time.”

```html
<!DOCTYPE html>
<html lang="en">
<head>
<meta charset="utf-8">
<title>Velmora Care – In-Center Hemodialysis Flyer</title>
<link href="https://fonts.googleapis.com/css2?family=Lato:wght@300;700;900&family=Lexend:wght@300;400;500;600;700&display=swap" rel="stylesheet">
<style>
  :root{
    --green:#6aa84f;
    --green-dark:#5d9a45;
    --blue:#3a6fb5;
    --blue-deep:#3465ad;
    --teal:#4f8f9a;
    --ink:#2b2b2b;
    --white:#ffffff;
    --stage:#5e5e5e;
    --lavender:#a9b3d8;
    --lavender-light:#c9cfe6;
  }
  html,body{margin:0;padding:0;overflow:hidden;}
  body{width:1200px;height:2192px;background:var(--stage);position:relative;font-family:"Lexend",sans-serif;}
  .flyer{position:absolute;left:50px;top:385px;width:897px;height:1160px;background:var(--white);
    transform:scale(1.2263);transform-origin:0 0;overflow:hidden;box-shadow:0 20px 40px rgba(0,0,0,.35);}
  .abs{position:absolute;}
  .hero-photo{left:498px;top:0;width:399px;height:337px;
    background:linear-gradient(135deg,#d9dde6 0%,#b8c3d6 40%,#6d8cc2 75%,#4a70b3 100%);}
  .clinic-photo{left:498px;top:337px;width:399px;height:823px;border-bottom-left-radius:150px;
    background:linear-gradient(180deg,#9fb0d8 0%,var(--lavender) 45%,var(--lavender-light) 80%,#b7bedc 100%);}
  .band-top{left:0;top:202px;width:498px;height:135px;
    background:linear-gradient(90deg,var(--green) 0%,var(--teal) 55%,var(--blue) 100%);}
  .band-main{left:0;top:337px;width:897px;height:163px;border-radius:0 0 90px 90px;
    background:linear-gradient(90deg,var(--green) 0%,#5b9a7c 35%,#3f7aa3 60%,rgba(52,101,173,.92) 100%);}
  .brand{left:62px;top:140px;font-family:"Lexend",sans-serif;font-weight:600;font-size:30px;color:var(--blue);
    display:flex;align-items:center;gap:12px;}
  .brand-mark{width:22px;height:22px;background:var(--green);display:inline-block;}
  .tagline{left:62px;top:218px;color:var(--white);font-family:"Lato",sans-serif;margin:0;}
  .tagline strong{display:block;font-weight:900;font-size:62px;line-height:62px;}
  .tagline span{display:block;font-weight:300;font-size:52px;line-height:56px;margin-top:12px;}
  .service-title{left:62px;top:540px;margin:0;font-weight:700;font-size:50px;line-height:48px;}
  .service-title .l1{color:var(--green);display:block;}
  .service-title .l2{color:var(--blue);display:block;}
  .rule{left:0;top:648px;width:450px;height:3px;background:var(--green);}
  .body-copy{left:62px;top:672px;width:420px;font-size:19.5px;line-height:26px;color:var(--ink);font-weight:300;}
  .body-copy p{margin:0 0 20px;}
  .hl{color:var(--blue);font-weight:500;}
  .info-box{left:520px;top:597px;width:313px;height:316px;border-radius:14px;background:rgba(52,101,173,.93);
    color:var(--white);box-sizing:border-box;padding:34px 20px 0 34px;font-size:19px;line-height:27px;font-weight:300;}
  .info-box b{font-weight:600;font-size:24px;}
  .info-box .accent{color:#7cc35a;font-weight:600;font-size:24px;}
  .info-box .loc{font-weight:600;font-size:25px;line-height:34px;}
  .insurance{left:518px;top:930px;width:379px;height:97px;background:var(--green);display:flex;align-items:center;
    padding-left:30px;box-sizing:border-box;gap:12px;color:var(--white);font-size:18.5px;font-weight:300;}
  .footer{left:0;top:1010px;width:897px;height:150px;background:var(--green);border-top-left-radius:130px;}
  .footer-cut{left:498px;top:1010px;width:399px;height:150px;border-bottom-left-radius:150px;
    background:linear-gradient(180deg,#c3c9e2 0%,#b7bedc 100%);}
  .cta{left:95px;top:1030px;color:var(--white);}
  .cta .now{font-size:25px;font-weight:500;line-height:26px;display:block;}
  .cta .more{font-size:11px;font-weight:300;display:block;text-align:right;}
  .phone{left:255px;top:1034px;width:242px;height:34px;border-radius:8px;background:var(--blue);color:var(--white);
    font-weight:600;font-size:29px;line-height:34px;text-align:center;letter-spacing:.5px;}
  .web{left:95px;top:1080px;font-size:18px;color:var(--white);}
  .web .lbl{color:var(--blue);}
</style>
</head>
<body>
<div class="flyer">
  <div class="abs hero-photo" role="img" aria-label="Photo of a nurse checking a dialysis patient's blood pressure"></div>
  <div class="abs clinic-photo" role="img" aria-label="Soft background photo of a bright dialysis treatment room"></div>
  <div class="abs footer"></div>
  <div class="abs footer-cut" role="img" aria-label="Continuation of the treatment room photo"></div>

  <div class="abs brand"><span class="brand-mark"></span>Velmora Care</div>

  <div class="abs band-top"></div>
  <div class="abs band-main"></div>
  <h1 class="abs tagline"><strong>Transforming<br>Lives,</strong><span>One Dialysis<br>Session at a Time</span></h1>

  <h2 class="abs service-title"><span class="l1">IN-CENTER</span><span class="l2">HEMODIALYSIS</span></h2>
  <div class="abs rule"></div>
  <div class="abs body-copy">
    <p>We offer <span class="hl">In-center hemodialysis</span> for renal patients who prefer to have their treatments at a dialysis center.</p>
    <p>Our dialysis center has <span class="hl">6 Nephrova Dialysis Machines</span>, supported by our state of the art water purification system.</p>
    <p><span class="hl">Pick up and drop off</span> of patients is an additional service we offer for all in-center hemodialysis patients.</p>
  </div>

  <div class="abs info-box">
    Once you're a<br><b>Dialysis Patient</b><br>with <span class="accent">Velmora,</span><br>You can also dialyze at any or our partner locations in <span class="loc">Trinidad<br>(Chaguanas<br>and Piarco)</span>
  </div>

  <div class="abs insurance">
    <svg width="34" height="34" viewBox="0 0 34 34" aria-hidden="true"><rect x="2" y="2" width="30" height="30" rx="3" fill="none" stroke="#fff" stroke-width="2.5"/><path d="M9 17l6 7 11-15" fill="none" stroke="#fff" stroke-width="3" stroke-linecap="round" stroke-linejoin="round"/></svg>
    We Accept All Insurance
  </div>

  <div class="abs cta"><span class="now">Call us now</span><span class="more">for more information!</span></div>
  <div class="abs phone">868-555-0142</div>
  <div class="abs web"><span class="lbl">Visit Our Website:</span> www.velmoracare.example</div>
</div>
</body>
</html>
```